World leading Water filters German made

I am a local Plumbing business who is authorised water filter installer
I want to do a Flyer design double sided targeting niche market for Water Filters.
My company colours are black background with white writing.
( but happy to go into different colours to capture more people )
I want all my stuff, sleek and professional with the same fonts throughout.
Www.brightvalepipeworks.au
Is my website you can see how I do things there.
I want the local business awards finalist logo on the flyer too ( it’ll be in the photo)
This Flyer I want all about health and wellness making big points on water filtration benefits
Massive to included HYDROGEN WATER AND ALKALINE WATER ,
REMOVE FLUORIDE
I don’t know whether to have it with the pre-save branded information I sent over, but I don’t want the company other companies name everywhere
I want the main focus about my company Brightvale Pipeworks And Boiler Experts
I want the focus to be about a family owned and run Illawarra local business establish for over 20 years.
Please note I have included a Customer brochure the company has designed so you can see some key points on the second page about the products. I want this a lot more eye-catching and appealing please
Target Market(s)
Health and wellness people
Colors
Designer to choose colors to be used in the design.
Requirements
Must have
- Call Trevor 0487 263 915, my website , social media buttons ,
Nice to have
- World leading , health and wellness ,
Should not have
- Any information to lead them away from calling myself , I’m the authorities dealer for aqua crest supply but I want to no have as much anout them.

```html
<!DOCTYPE html>
<html lang="en">
<head>
<meta charset="utf-8">
<title>Brightvale Pipeworks Water Filter Flyer</title>
<link rel="stylesheet" href="https://fonts.googleapis.com/css2?family=Archivo:wdth,wght@62..125,300..900&family=Poppins:wght@400;500;600&display=swap">
<style>
:root{
  --red:#d9151c;
  --red-dark:#a50f14;
  --ink:#161616;
  --black:#0e0e0e;
  --white:#ffffff;
  --paper-grey:#efefef;
  --box-grey:#e9e9e9;
  --rule:#d6d6d6;
  --stage:#e8e8e8;
  --gold-1:#f3e2b0;
  --gold-2:#c9a865;
  --gold-3:#8f7238;
}
*{margin:0;padding:0;box-sizing:border-box}
html,body{width:815px;height:1200px;overflow:hidden;background:var(--stage)}
body{position:relative;font-family:"Poppins",sans-serif;color:var(--ink)}
.sheet{position:absolute;left:201px;width:412px;height:580px;overflow:hidden;box-shadow:0 4px 14px rgba(0,0,0,.18)}
.sheet--front{top:13px}
.sheet--back{top:607px}
.sheet__inner{position:absolute;left:0;top:0;width:545px;height:767px;transform:scale(.756);transform-origin:0 0;background:var(--white)}
.abs{position:absolute}
.display{font-family:"Archivo",sans-serif;font-weight:900;font-stretch:125%;text-transform:uppercase;line-height:1}

/* front */
.hero-photo{left:0;top:0;width:545px;height:305px;background:linear-gradient(160deg,#2a2424 0%,#1a1717 45%,#2e2a28 75%,#151313 100%)}
.brand{left:0;top:34px;width:545px;display:flex;justify-content:center;align-items:center;gap:8px}
.brand__mark{width:12px;height:12px;background:var(--white)}
.brand__name{font-family:"Archivo",sans-serif;font-weight:800;font-stretch:125%;font-size:19px;color:var(--white);letter-spacing:.5px}
.headline{left:0;top:104px;width:545px;text-align:center}
.headline__lead{display:block;font-size:19.5px;color:var(--white);letter-spacing:.2px}
.headline__main{display:block;font-size:44px;color:var(--red);margin-top:8px;line-height:1}
.hero-sub{left:40px;top:238px;width:465px;text-align:center;color:var(--white);font-size:11.5px;line-height:1.3}
.award-plate{left:36px;top:285px;width:138px;height:257px;background:var(--red)}
.award-plate__band{left:0;top:193px;width:138px;height:2px;background:var(--white)}
.award-seal{left:18px;top:292px;width:176px;height:176px;border-radius:50%;background:radial-gradient(circle at 38% 32%,var(--gold-1) 0%,var(--gold-2) 55%,var(--gold-3) 100%);box-shadow:0 3px 8px rgba(0,0,0,.35)}
.award-seal__core{left:40px;top:40px;width:96px;height:96px;border-radius:50%;background:radial-gradient(circle at 40% 35%,#efe0b8,#bfa064)}
.need-box{left:190px;top:307px;width:328px;height:112px;background:var(--box-grey)}
.need-title{left:216px;top:325px;width:290px;font-family:"Archivo",sans-serif;font-weight:800;font-stretch:110%;font-size:14.5px;color:var(--red);line-height:1.1;text-transform:uppercase}
.need-copy{left:216px;top:368px;width:290px;font-size:8.5px;line-height:1.35}
.about-title{left:216px;top:432px;font-family:"Archivo",sans-serif;font-weight:800;font-stretch:110%;font-size:11.5px;text-transform:uppercase}
.about-title span{color:var(--red)}
.about-copy{left:216px;top:452px;width:290px;font-size:7.6px;line-height:1.35}
.about-copy p+p{margin-top:9px}
.call-title{left:36px;top:572px;font-size:16px;font-weight:900;font-stretch:112%;color:var(--ink);line-height:1.08}
.badge-247{left:318px;top:560px;width:162px;height:52px}
.call-copy{left:36px;top:623px;width:480px;font-size:7.6px;line-height:1.35}
.footer{left:0;width:545px;height:64px;background:var(--black)}
.sheet--front .footer{top:703px}
.footer__cta{left:0;top:15px;width:200px;height:34px;background:var(--red);clip-path:polygon(0 0,100% 0,95% 100%,0 100%);display:flex;align-items:center;padding-left:24px}
.footer__cta span{font-family:"Archivo",sans-serif;font-weight:400;font-stretch:125%;font-size:14px;color:var(--white);letter-spacing:.6px;text-transform:uppercase}
.footer__phone{left:212px;top:18px;display:flex;align-items:center;gap:6px;color:var(--white);font-size:19px;font-weight:400}
.footer__web{left:400px;top:14px;display:flex;align-items:center;gap:5px;color:var(--white);font-size:7px}
.social{left:400px;top:32px;display:flex;align-items:center;gap:6px;color:var(--white);font-size:7px}
.social__btn{width:13px;height:13px;border-radius:50%;border:1.2px solid var(--white)}

/* back */
.back-right{left:265px;top:0;width:280px;height:767px;background:var(--paper-grey)}
.benefits-title{left:37px;top:36px;font-size:27px;color:var(--red)}
.benefit{left:30px;width:215px}
.benefit__icon{position:absolute;left:0;top:0;width:34px;height:34px}
.benefit__title{position:absolute;left:51px;top:0;font-family:"Archivo",sans-serif;font-weight:800;font-stretch:110%;font-size:17px;white-space:nowrap}
.benefit__list{position:absolute;left:51px;top:25px;list-style:none;font-size:7.6px;line-height:12.7px}
.benefit__list li{position:relative;padding-left:10px;white-space:nowrap}
.benefit__list li::before{content:"";position:absolute;left:0;top:4px;width:4px;height:4px;border:1px solid var(--red);border-radius:50%}
.divider{left:0;width:240px;height:1px;background:var(--rule)}
.svc-title{left:293px;top:33px;font-size:16px;line-height:1.05}
.svc-title span{color:var(--red)}
.svc-copy{left:294px;width:228px;font-size:7.6px;line-height:1.33}
.svc-copy p+p{margin-top:9px}
.sub-title{left:294px;font-family:"Archivo",sans-serif;font-weight:400;font-stretch:115%;font-size:11px;color:var(--red);line-height:1.1;text-transform:uppercase}
.photo{left:290px;width:212px}
.photo--sink{top:204px;height:103px;background:linear-gradient(120deg,#3c3a38 0%,#d9d9d9 40%,#f2f2f2 55%,#2e5fb0 78%,#1f3f7a 100%)}
.photo--tank{top:576px;height:100px;background:linear-gradient(90deg,#8a4a36 0%,#a35a40 25%,#bfbfbf 45%,#9a9a9a 60%,#c9c9c9 75%,#7a4535 100%)}
.sheet--back .footer{top:702px}
</style>
</head>
<body>

<section class="sheet sheet--front" aria-label="Flyer front">
  <div class="sheet__inner">
    <div class="abs hero-photo" role="img" aria-label="Dark photo of a plumber's van with water filter units"></div>
    <div class="abs brand"><span class="brand__mark"></span><span class="brand__name">BRIGHTVALE PIPEWORKS</span></div>
    <h1 class="abs headline display">
      <span class="headline__lead">Your true local plumber</span>
      <span class="headline__main">Pure, healthy<br>filtered water</span>
    </h1>
    <p class="abs hero-sub">Authorised water filter installers bringing healthier water to homes in the Illawarra, Wollongong, Shellharbour &amp; Shoalhaven areas.</p>

    <div class="abs need-box"></div>
    <div class="abs award-plate"><div class="abs award-plate__band"></div></div>
    <div class="abs award-seal" role="img" aria-label="Local business awards finalist seal"><div class="abs award-seal__core"></div></div>

    <h2 class="abs need-title">Want healthier water<br>for your family?</h2>
    <p class="abs need-copy">With over 20 years in the plumbing industry, we install world leading German made water filters for hydrogen rich, alkaline, fluoride free water.</p>

    <h3 class="abs about-title"><span>About</span> Us</h3>
    <div class="abs about-copy">
      <p>Brightvale Pipeworks is a family owned and run Illawarra local business, established for over 20 years and serving Wollongong, Shellharbour and Shoalhaven.</p>
      <p>As authorised water filter installers, we take pride in a friendly, honest and affordable service. Our filters remove fluoride, chlorine and heavy metals, giving your family cleaner water for better health and wellness.</p>
    </div>

    <h2 class="abs call-title display">Call Trevor anytime<br>water filter experts</h2>
    <svg class="abs badge-247" viewBox="0 0 162 52" aria-label="24/7 service">
      <path d="M6 6 Q81 -4 156 6 L150 44 Q81 36 12 44 Z" fill="var(--red)"/>
      <path d="M12 44 L18 51 L22 40 Z" fill="var(--red-dark)"/>
      <path d="M150 44 L144 51 L140 40 Z" fill="var(--red-dark)"/>
      <path d="M44 12 c-3 0 -5 3 -4 6 c2 6 6 10 12 12 c3 1 6 -1 6 -4 l-4 -3 l-3 2 c-3 -1 -5 -3 -6 -6 l2 -3 z" fill="none" stroke="#fff" stroke-width="2"/>
      <text x="62" y="25" font-family="Archivo,sans-serif" font-weight="900" font-stretch="125%" font-size="20" fill="#fff">24/7</text>
      <text x="66" y="35" font-family="Archivo,sans-serif" font-weight="800" font-size="7.5" fill="#fff" letter-spacing="1">SERVICE</text>
    </svg>
    <p class="abs call-copy">Feel secure knowing our dedicated family team is just a call away. Call Trevor for expert advice on the right water filter for your home. With over 20 years of industry experience, we install and service world leading German made systems that deliver hydrogen rich, alkaline water and remove fluoride, chlorine, heavy metals and PFAS. Whether you want healthier drinking water, chemical free showering or relief for eczema and asthma, we go the extra mile with same-day service and local care you can trust.</p>

    <footer class="abs footer">
      <div class="abs footer__cta"><span>Call Trevor</span></div>
      <div class="abs footer__phone">
        <svg width="16" height="16" viewBox="0 0 24 24" aria-hidden="true"><path d="M6 3 c-2 0 -3 2 -3 4 c1 8 7 14 15 15 c2 0 4 -1 4 -3 l-4 -4 l-3 2 c-3 -1 -6 -4 -7 -7 l2 -3 z" fill="none" stroke="#fff" stroke-width="1.8"/></svg>
        <span>0487 263 915</span>
      </div>
      <div class="abs footer__web">
        <svg width="11" height="11" viewBox="0 0 24 24" aria-hidden="true"><circle cx="12" cy="12" r="10" fill="none" stroke="#fff" stroke-width="1.8"/><ellipse cx="12" cy="12" rx="4.5" ry="10" fill="none" stroke="#fff" stroke-width="1.5"/><line x1="2" y1="12" x2="22" y2="12" stroke="#fff" stroke-width="1.5"/></svg>
        <span>brightvalepipeworks.au</span>
      </div>
      <div class="abs social" aria-label="Social media">
        <span class="social__btn"></span><span class="social__btn"></span><span class="social__btn"></span>
        <span>Follow us</span>
      </div>
    </footer>
  </div>
</section>

<section class="sheet sheet--back" aria-label="Flyer back">
  <div class="sheet__inner">
    <div class="abs back-right"></div>

    <h2 class="abs benefits-title display">Benefits</h2>

    <div class="abs benefit" style="top:92px">
      <svg class="benefit__icon" viewBox="0 0 34 34" aria-hidden="true"><path d="M17 3 L28 7 V16 C28 23 23 28 17 31 C11 28 6 23 6 16 V7 Z" fill="none" stroke="var(--red)" stroke-width="1.6"/><path d="M12 17 l4 4 l7 -8" fill="none" stroke="var(--red)" stroke-width="1.6"/></svg>
      <h3 class="benefit__title">Health Benefits</h3>
      <ul class="benefit__list">
        <li>Reduce the risk of cancer</li><li>Relief for eczema sufferers</li><li>Anti-Aging benefits</li><li>Reduce the risk of birth defects</li><li>Relief for asthma sufferers</li><li>Enjoy chemical free showering</li><li>Healthier drinking water</li><li>Alkaline water</li><li>Hydrogen rich water</li>
      </ul>
    </div>
    <div class="abs divider" style="top:237px"></div>

    <div class="abs benefit" style="top:249px">
      <svg class="benefit__icon" viewBox="0 0 34 34" aria-hidden="true"><circle cx="9" cy="25" r="4.5" fill="none" stroke="var(--red)" stroke-width="1.6"/><circle cx="24" cy="25" r="4.5" fill="none" stroke="var(--red)" stroke-width="1.6"/><path d="M9 19 V6 M5 10 L9 6 L13 10 M24 19 V6 M20 10 L24 6 L28 10 M16.5 16 V9" fill="none" stroke="var(--red)" stroke-width="1.6"/></svg>
      <h3 class="benefit__title">Remove &amp; Improve</h3>
      <ul class="benefit__list">
        <li>Chlorine 99.99%</li><li>Chloramine 99.99%</li><li>Fluoride</li><li>Heavy Metals</li><li>Bacteria</li><li>Parasites</li><li>Pesticides</li><li>Hard Water</li><li>PFA'S</li>
      </ul>
    </div>
    <div class="abs divider" style="top:394px"></div>

    <div class="abs benefit" style="top:408px">
      <svg class="benefit__icon" viewBox="0 0 34 34" aria-hidden="true"><circle cx="17" cy="9" r="4" fill="none" stroke="var(--red)" stroke-width="1.6"/><path d="M10 30 V19 C10 15 24 15 24 19 V30" fill="none" stroke="var(--red)" stroke-width="1.6"/><circle cx="5" cy="14" r="3" fill="none" stroke="var(--red)" stroke-width="1.4"/><circle cx="29" cy="14" r="3" fill="none" stroke="var(--red)" stroke-width="1.4"/></svg>
      <h3 class="benefit__title">Extend the life</h3>
      <ul class="benefit__list">
        <li>Hot Water Systems</li><li>Washing machine</li><li>Dishwasher</li><li>Tapware</li><li>Bathrooms</li><li>Plumbing</li><li>Home appliances</li>
      </ul>
    </div>
    <div class="abs divider" style="top:530px"></div>

    <div class="abs benefit" style="top:542px">
      <svg class="benefit__icon" viewBox="0 0 34 34" aria-hidden="true"><circle cx="13" cy="9" r="5" fill="none" stroke="var(--red)" stroke-width="1.6"/><path d="M3 28 C3 19 23 19 23 28" fill="none" stroke="var(--red)" stroke-width="1.6"/><circle cx="25" cy="24" r="5" fill="none" stroke="var(--red)" stroke-width="1.6"/><path d="M22 29 L21 33 L25 31 L29 33 L28 29" fill="none" stroke="var(--red)" stroke-width="1.4"/></svg>
      <h3 class="benefit__title">World Leading</h3>
      <ul class="benefit__list">
        <li>Australian, German &amp;<br>Japanese Designed</li><li>100% Renewable</li><li>100% Sustainable</li><li>1000% Greater Absorption</li><li>Robust Design</li><li>Robust Warranty</li><li>Adopted throughout Europe<br>and the USA</li>
      </ul>
    </div>

    <h2 class="abs svc-title display">Our water filter<br><span>services</span></h2>
    <div class="abs svc-copy" style="top:76px">
      <p>We are a family owned and run Illawarra business, established for over 20 years and authorised to install world leading German made water filters. Whether you have a question about the right system for your home or want to book an install, don't hesitate to call Trevor. We deeply care about your family's health and wellness, and our commitment to quality shines through in every filter we fit. From the kitchen tap to the whole house, we'll make sure you enjoy cleaner, softer, healthier water every day. And remember, if you have any questions, our friendly team is always just a phone call away.</p>
    </div>
    <div class="abs photo photo--sink" role="img" aria-label="Photo of a plumber fitting a water filter beneath a kitchen sink"></div>

    <h3 class="abs sub-title" style="top:342px">Hydrogen &amp; alkaline<br>water</h3>
    <div class="abs svc-copy" style="top:370px">
      <p>Enjoy hydrogen rich, alkaline water straight from your tap. Rich in antioxidants and gentle on the body, it supports hydration, anti-aging and everyday wellness, giving your whole family better tasting water that is good for you.</p>
    </div>
    <h3 class="abs sub-title" style="top:448px">Remove fluoride</h3>
    <div class="abs svc-copy" style="top:467px">
      <p>Our whole house filters remove fluoride, chlorine, chloramine, heavy metals and PFAS, so you can drink, cook and shower in clean, chemical free water.</p>
      <p>We handle everything from expert installation to regular servicing, keeping your filter working at its best and protecting your appliances for years.</p>
    </div>
    <div class="abs photo photo--tank" role="img" aria-label="Photo of whole house water filter units installed against a brick wall"></div>

    <footer class="abs footer">
      <div class="abs footer__cta"><span>Call Trevor</span></div>
      <div class="abs footer__phone">
        <svg width="16" height="16" viewBox="0 0 24 24" aria-hidden="true"><path d="M6 3 c-2 0 -3 2 -3 4 c1 8 7 14 15 15 c2 0 4 -1 4 -3 l-4 -4 l-3 2 c-3 -1 -6 -4 -7 -7 l2 -3 z" fill="none" stroke="#fff" stroke-width="1.8"/></svg>
        <span>0487 263 915</span>
      </div>
      <div class="abs footer__web">
        <svg width="11" height="11" viewBox="0 0 24 24" aria-hidden="true"><circle cx="12" cy="12" r="10" fill="none" stroke="#fff" stroke-width="1.8"/><ellipse cx="12" cy="12" rx="4.5" ry="10" fill="none" stroke="#fff" stroke-width="1.5"/><line x1="2" y1="12" x2="22" y2="12" stroke="#fff" stroke-width="1.5"/></svg>
        <span>brightvalepipeworks.au</span>
      </div>
      <div class="abs social" aria-label="Social media">
        <span class="social__btn"></span><span class="social__btn"></span><span class="social__btn"></span>
        <span>Follow us</span>
      </div>
    </footer>
  </div>
</section>

</body>
</html>
```